BrightHearth Flyer

A simple flyer that gets people attention
I have a attached a sample of what we use now and a picture we use
We service gas fireplaces and need a eye catching but not to cluttered flyer to promote our business. the cost per fireplace should be $60.00
Updates

Project Deadline Extended
Reason: Sorry for the delay We are out of town on holidays with sketchy internet service To frustrating to complete this project till I am back in a week Thank you for your patience Kind regards Dale

```html
<!DOCTYPE html>
<html lang="en">
<head>
<meta charset="utf-8">
<title>BrightHearth Gas Services Flyer</title>
<link rel="stylesheet" href="https://fonts.googleapis.com/css2?family=Carlito:ital,wght@0,400;0,700;1,400&family=Fira+Sans+Extra+Condensed:ital,wght@1,800&family=Noticia+Text:ital@1&display=swap">
<style>
  :root {
    --stage: #e4e4e6;
    --orange: #e2561f;
    --orange-top: #e8652a;
    --ember: #3a2418;
    --ember-warm: #8a4a26;
    --flame: #d9792a;
    --white: #ffffff;
    --rule: rgba(255,255,255,0.6);
  }
  * { margin: 0; padding: 0; box-sizing: border-box; }
  html, body { width: 1200px; height: 900px; overflow: hidden; }
  body { background: var(--stage); font-family: "Carlito", "Calibri", sans-serif; }
  .flyer {
    position: absolute; left: 289px; top: 40px; width: 622px; height: 803px;
    background: var(--orange); overflow: hidden; color: var(--white);
  }
  .flyer__topband { position: absolute; left: 0; top: 0; width: 100%; height: 17px; background: var(--orange-top); }
  .flyer__photo {
    position: absolute; left: 0; top: 17px; width: 100%; height: 500px;
    background:
      radial-gradient(ellipse 30% 22% at 52% 30%, var(--flame) 0%, rgba(217,121,42,0) 100%),
      radial-gradient(ellipse 45% 40% at 30% 70%, #c9a08a 0%, rgba(201,160,138,0) 100%),
      radial-gradient(ellipse 30% 40% at 85% 60%, #b98d76 0%, rgba(185,141,118,0) 100%),
      linear-gradient(180deg, var(--ember) 0%, var(--ember-warm) 45%, #5a3524 100%);
  }
  .flyer__textband {
    position: absolute; left: 0; top: 385px; width: 100%; height: 133px;
    background: linear-gradient(180deg, rgba(60,30,20,0.55), rgba(80,35,20,0.6));
  }
  .brand {
    position: absolute; left: 12px; top: 66px; width: 96px;
    display: flex; flex-direction: column; align-items: center; gap: 6px;
  }
  .brand__mark { width: 14px; height: 14px; background: var(--orange); }
  .brand__name { font-weight: 700; font-size: 14px; line-height: 16px; color: var(--white); white-space: nowrap; }
  .title-rule { position: absolute; left: 116px; top: 35px; width: 2px; height: 107px; background: var(--white); }
  .title {
    position: absolute; left: 127px; top: 38px;
    font-family: "Fira Sans Extra Condensed", sans-serif; font-style: italic; font-weight: 800;
    font-size: 35px; line-height: 31px; text-transform: uppercase; letter-spacing: 0.2px;
  }
  .body-copy {
    position: absolute; left: 8px; top: 394px; width: 592px;
    column-count: 2; column-gap: 9px;
    font-size: 11.9px; line-height: 14.6px; text-align: justify; hyphens: auto;
  }
  .body-copy p { margin: 0; }
  .price { position: absolute; left: 0; top: 625px; width: 100%; text-align: center; }
  .price__amount {
    font-family: "Fira Sans Extra Condensed", sans-serif; font-style: italic; font-weight: 800;
    font-size: 41px; line-height: 44px; text-shadow: 2px 2px 3px rgba(80,20,0,0.6);
  }
  .price__tax {
    position: absolute; left: 362px; top: 38px;
    font-family: "Noticia Text", serif; font-style: italic; font-size: 13px;
  }
  .rule { position: absolute; left: 141px; width: 336px; height: 1px; background: var(--rule); }
  .rule--top { top: 687px; }
  .rule--bottom { top: 732px; }
  .payment-note {
    position: absolute; left: 0; top: 691px; width: 100%; text-align: center;
    font-family: "Noticia Text", serif; font-style: italic; font-size: 15px; line-height: 19px;
  }
  .contact { position: absolute; left: 0; top: 740px; width: 100%; text-align: center; }
  .contact__lead { font-size: 17px; line-height: 22px; }
  .contact__line { font-size: 20.5px; line-height: 26px; font-weight: 700; }
</style>
</head>
<body>
  <main class="flyer">
    <div class="flyer__topband"></div>
    <div class="flyer__photo" role="img" aria-label="Photo of a family's bare feet warming in front of a glowing gas fireplace"></div>
    <div class="flyer__textband"></div>

    <div class="brand">
      <span class="brand__mark"></span>
      <span class="brand__name">BrightHearth</span>
    </div>
    <div class="title-rule"></div>
    <h1 class="title">Notice to the<br>owners name<br>of property</h1>

    <div class="body-copy">
      <p>BRIGHTHEARTH GAS SERVICES will be on site conducting gas fireplace safety inspections and maintenance for NAME OF PROPERTY on DATE OF SERVICE. If you wish to have your fireplace serviced, please put your name and unit number on the sign-up sheet provided. We will require approximately 20 - 30 minutes to service each fireplace and require that the fireplace is cool to conduct the work. Please do not use your fireplace within 2 hours of your appointment as we do not want the technicians to receive burns.</p>
      <p>The National Energy Efficiency Office states that all fireplaces require regular servicing. Fireplace manufacturers recommend each unit be serviced annually by a qualified technician and insurance companies and Fire Departments are now asking for reports regarding fireplace safety inspections and servicing. The service BrightHearth Gas Services will provide will entail a thorough assessment of pilot, burner and valve operation, a door seal inspection, an inspection of the electrical circuits, repositioning of the logs, cleaning and adjustment of fan and controls, cleaning of the firebox and glass, a carbon monoxide test, testing of fittings for gas leaks and a complete operational test once the service is complete.</p>
      <p>Possible indication that your gas fireplace requires service include: (1) Cloudy film on glass, (2) Strong odors when fireplace is in operation, (3) Soot build up on glass, logs or exterior of building, (4) Tarnished/discolored brass, (5) Pilot light outages, (6) Main burner is not lighting consistently, (7) Delayed ignition, and (8) Flames are not evenly dispersed.</p>
    </div>

    <div class="price">
      <div class="price__amount">THE COST IS $60.00</div>
      <div class="price__tax">(tax included)</div>
    </div>
    <div class="rule rule--top"></div>
    <p class="payment-note">(Owners must have payment ready at time of inspection. Payment may be<br>made in the form of cash, cheque or credit card)</p>
    <div class="rule rule--bottom"></div>

    <div class="contact">
      <p class="contact__lead">For further information please contact Renata at:</p>
      <p class="contact__line">BrightHearth Gas Services 604.555.0187</p>
    </div>
  </main>
</body>
</html>
```